New Start Up Website for Volt Ranger Mobile - Mobile EV Charging

I need an informational website built to support my new start up. Should be clean and very straight forward. Home, About, Vehicles we Support, Links to iOS and Android apps, Contact Us. Volt Ranger Mobile is an emergency / express EV charging solution. Charging as a Service as the industry is being dubbed. I believe I am second to market next to Brisk Amp and their Surgely mobile solution.
Updates

Website must be built on Wordpress!

Target Market(s)

EV Owners

Industry/Entity Type

EV Charging

Coding

Coded - Design and coding required

Number of Pages Required

4 page

Font styles to use
Sans Serif

Colors
59FF00
82FF00
B8FF75
E3FFCB
F4FFEA

Requirements
Must have
• I will not have any real pics for at least 60 days. I will need place holders or a mock up of the vehicle.
Nice to have
• Briskamp.io is our competitor. They own Surgely APP which is what we're modeling.

```html
<!DOCTYPE html>
<html lang="en">
<head>
<meta charset="utf-8">
<title>Volt Ranger Mobile – Express EV Charging</title>
<link rel="stylesheet" href="https://fonts.googleapis.com/css2?family=Raleway:wght@400;500;600;700;800&family=Roboto:wght@400;500;700&display=swap">
<style>
:root{
  --green:#3fbf12;
  --green-bright:#59ff00;
  --lime:#82ff00;
  --blue:#1649e6;
  --navy:#0b1628;
  --ink:#1b1b1b;
  --muted:#7a7a7a;
  --line:#e4e6ea;
  --soft:#f7f8fa;
  --footer:#1f2022;
}
*{box-sizing:border-box;margin:0;padding:0}
html,body{width:1200px;height:4545px;overflow:hidden}
body{font-family:"Roboto",sans-serif;color:var(--ink);background:#fff;position:relative}
.abs{position:absolute}
h1,h2,h3,h4{font-family:"Raleway",sans-serif;font-weight:500}
.eyebrow{font-family:"Roboto",sans-serif;font-size:13px;font-weight:500;letter-spacing:.5px;text-transform:uppercase;color:#333}
.section-title{font-size:33px;color:#111}
.center{text-align:center;left:0;width:1200px}
.btn{display:inline-flex;align-items:center;justify-content:center;background:var(--green);color:#fff;font-size:11px;font-weight:700;border-radius:20px;letter-spacing:.4px}
.ph{display:block}

/* top bar */
.topbar{top:0;left:0;width:1200px;height:58px;background:#fff}
.brand{font-family:"Raleway",sans-serif;font-weight:800;font-size:14px;color:var(--blue);display:flex;align-items:center;gap:8px;text-transform:uppercase}
.brand-dot{width:14px;height:14px;border-radius:50%;background:var(--green)}
.contact-chip{display:flex;gap:12px;align-items:center}
.chip-icon{width:26px;height:26px;background:#fff;box-shadow:0 2px 6px rgba(0,0,0,.12);border-radius:3px;display:flex;align-items:center;justify-content:center}
.chip-label{font-size:11px;font-weight:500;color:#222}
.chip-value{font-size:9px;color:#777;margin-top:3px}

/* nav */
.nav{top:58px;left:0;width:1200px;height:41px;background:var(--navy)}
.nav-links{left:129px;top:0;height:41px;display:flex;align-items:center;gap:37px;font-size:11px;color:#fff;text-transform:uppercase;letter-spacing:.2px}
.nav-links .active{color:var(--green-bright)}
.nav-call{right:130px;top:0;height:41px;display:flex;align-items:center;gap:6px;font-size:10px;color:var(--lime)}

/* hero */
.hero{top:99px;left:0;width:1200px;height:467px;background:linear-gradient(100deg,#3d4048 0%,#6b6a6b 28%,#20242b 48%,#2e3a52 60%,#b5743f 88%,#d28f4a 100%)}
.hero-title{left:699px;top:140px;font-family:"Raleway",sans-serif;font-weight:800;font-size:50px;line-height:58px;color:#fff;text-transform:uppercase}
.hero-copy{left:700px;top:266px;width:380px;font-size:13px;line-height:19px;color:#fff}
.hero-btn{left:700px;top:323px;width:132px;height:38px;font-size:12px}
.hero-arrow{top:214px;width:20px;height:40px}

/* about */
.about-bar{left:130px;top:661px;width:3px;height:96px;background:var(--blue)}
.about-eyebrow{left:144px;top:661px}
.about-title{left:144px;top:680px;font-size:33px;line-height:41px}
.about-copy{left:130px;top:786px;width:450px;font-size:11.5px;line-height:19px;color:#555}
.about-list{left:130px;top:888px;list-style:none;font-size:11px;color:#333}
.about-list li{display:flex;align-items:center;gap:7px;height:28px}
.about-list li::before{content:"";width:8px;height:8px;background:var(--blue);border-radius:2px}
.about-btn{left:130px;top:989px;width:108px;height:33px;font-size:9px}
.about-photo{left:626px;top:632px;width:401px;height:421px;border-radius:14px;background:linear-gradient(160deg,#9fb7cf 0%,#c9d3dc 35%,#4b5766 65%,#2a2f37 100%)}
.exp-tab{left:599px;top:690px;width:56px;height:303px;background:var(--blue);border-radius:10px 0 0 10px;display:flex;align-items:center;justify-content:center}
.exp-tab span{transform:rotate(-90deg);white-space:nowrap;color:#fff;font-size:15px;font-weight:500;letter-spacing:.6px}

/* services */
.svc-card{top:1209px;width:300px;height:284px;border:1px solid var(--line);background:var(--soft);box-shadow:0 2px 6px rgba(0,0,0,.05)}
.svc-card .svc-body{height:231px;text-align:center;padding-top:30px}
.svc-card h3{font-size:18px;margin:14px 0 14px}
.svc-card p{font-size:11px;line-height:17px;color:#555;padding:0 28px}
.svc-card .svc-foot{height:53px;border-top:1px solid var(--line);display:flex;align-items:center;justify-content:center;font-size:11px;font-weight:500;color:#3a55b5;background:#fff}
.svc-photo{height:231px;background:linear-gradient(120deg,#2a2624 0%,#d8d6d4 45%,#3e3230 75%,#6a4b3a 100%)}
.slide-btn{top:1340px;width:24px;height:24px;border:1px solid #ddd;background:#fff;display:flex;align-items:center;justify-content:center;font-size:11px;color:#444}

/* perks band */
.perks{top:1558px;left:0;width:1200px;height:284px;background:linear-gradient(90deg,#1b1d21 0%,#2c3035 40%,#4a4d52 70%,#2a1b1b 100%)}
.perk-num{width:22px;height:22px;border-radius:50%;background:var(--green);color:#fff;font-size:8px;display:flex;align-items:center;justify-content:center;font-weight:700}
.perk-title{font-family:"Raleway",sans-serif;font-size:19px;color:#fff}
.perk-copy{width:185px;font-size:10.5px;line-height:17px;color:#c9c9c9}

/* features */
.feat{width:300px}
.feat h4{font-size:16px;font-weight:600;margin-bottom:8px}
.feat p{font-size:11px;line-height:17px;color:#8a8a8a}
.feat.left{text-align:right}
.feat-icon{width:61px;height:61px;background:var(--blue);display:flex;align-items:center;justify-content:center}
.car{left:510px;top:2005px;width:210px;height:310px}

/* testimonial */
.testi-photo{top:2421px;left:0;width:1200px;height:420px;background:linear-gradient(90deg,#5a7090 0%,#b8c5d4 25%,#2c3445 50%,#c3ccd6 75%,#6e86a6 100%)}
.testi-card{left:671px;top:2370px;width:398px;height:348px;background:#f7f8f9;padding:40px 26px 0 26px}
.testi-text{font-size:11.5px;line-height:23px;color:#555;margin-top:22px}
.dots{right:40px;top:52px;display:flex;gap:7px}
.dots i{width:5px;height:5px;border-radius:50%;background:#cfd4da}
.dots i:first-child{background:var(--green)}
.avatar{width:50px;height:50px;border-radius:50%;background:linear-gradient(135deg,#c9a88a,#7a5a44)}
.stars{display:flex;gap:8px}

/* video */
.video{left:129px;top:2794px;width:940px;height:413px;background:linear-gradient(100deg,#4a5464 0%,#7b8594 35%,#3d444f 55%,#cfd3d8 80%,#9aa1ab 100%)}
.play{left:427px;top:175px;width:86px;height:56px;border:3px solid #fff;border-radius:28px;display:flex;align-items:center;justify-content:center}

/* articles */
.post{top:3358px;width:300px}
.post-img{height:213px}
.post-date{font-size:11px;color:var(--green);margin-top:23px}
.post-title{font-size:15px;color:#222;margin-top:8px}

/* quote */
.quote-photo{top:3738px;left:0;width:1200px;height:455px;background:linear-gradient(90deg,#4d4d52 0%,#d9d9db 20%,#a8a9ab 40%,#5f6a54 62%,#3d4a5f 78%,#7b8b6a 100%)}
.quote-card{left:129px;top:3689px;width:462px;height:349px;background:#fff;padding:44px 29px 0}
.quote-card h2{font-size:33px;color:#111}
.quote-card .sub{font-size:11.5px;color:#777;margin-top:8px}
.field{width:198px;height:34px;background:var(--soft);border:1px solid #eceef1;font-size:9px;color:#444;padding:11px 0 0 12px}
.field.area{height:128px}
.submit{width:198px;height:34px;background:var(--green);color:#fff;font-size:9px;display:flex;align-items:center;justify-content:center;letter-spacing:.4px}

/* footer */
.footer{top:4193px;left:0;width:1200px;height:352px;background:var(--footer);color:#d7d7d7}
.foot-brand{left:129px;top:60px;font-family:"Raleway",sans-serif;font-weight:800;font-size:14px;color:#fff;text-transform:uppercase}
.foot-about{left:129px;top:125px;width:245px;font-size:10.5px;line-height:17px;color:#bdbdbd}
.socials{left:129px;top:210px;display:flex;gap:20px}
.socials i{width:25px;height:25px;border-radius:50%;background:#fff;display:block}
.foot-col h5{font-family:"Roboto",sans-serif;font-size:12.5px;font-weight:500;color:var(--green-bright);text-transform:uppercase;margin-bottom:16px}
.foot-col ul{list-style:none;font-size:10.5px;color:#d0d0d0}
.foot-col li{height:26.5px}
.foot-contact{display:flex;gap:10px;align-items:flex-start;font-size:10.5px;line-height:14px;color:#d0d0d0;margin-bottom:18px}
.foot-contact .ring{width:24px;height:24px;border:1px solid #fff;border-radius:50%;display:flex;align-items:center;justify-content:center;flex:none}
.copyright{top:4476px;font-size:10.5px;color:#fff}
.copyright span{color:var(--green-bright)}
</style>
</head>
<body>

<!-- top bar -->
<header class="abs topbar">
  <div class="abs brand" style="left:129px;top:21px"><span class="brand-dot"></span>Volt Ranger Mobile</div>
  <div class="abs contact-chip" style="left:668px;top:15px">
    <div class="chip-icon"><svg width="10" height="13" viewBox="0 0 10 13"><path d="M5 0a5 5 0 0 0-5 5c0 3.5 5 8 5 8s5-4.5 5-8a5 5 0 0 0-5-5zm0 7a2 2 0 1 1 0-4 2 2 0 0 1 0 4z" fill="#3fbf12"/></svg></div>
    <div><div class="chip-label">HEAD OFFICE</div><div class="chip-value">48 Harbor Ln. Clearwater, NY 10820</div></div>
  </div>
  <div class="abs contact-chip" style="left:908px;top:15px">
    <div class="chip-icon" style="background:var(--green)"><svg width="12" height="9" viewBox="0 0 12 9"><rect x=".5" y=".5" width="11" height="8" fill="none" stroke="#fff"/><path d="M.5.5 6 5 11.5.5" fill="none" stroke="#fff"/></svg></div>
    <div><div class="chip-label">EMAIL</div><div class="chip-value">info@voltrangermobile.com</div></div>
  </div>
</header>

<!-- navigation -->
<nav class="abs nav">
  <div class="abs nav-links">
    <span class="active">Home</span><span>About</span><span>Vehicles We Support</span><span>iOS / Android Apps</span><span>Contact Us</span>
  </div>
  <div class="abs nav-call"><svg width="10" height="12" viewBox="0 0 10 12"><path d="M2 0h2l1 3-1.5 1a6 6 0 0 0 2.5 4l1-1.5 3 1v2a1.5 1.5 0 0 1-1.5 1.5A9 9 0 0 1 .5 1.5 1.5 1.5 0 0 1 2 0z" fill="#82ff00"/></svg>Call Us: +1 (555) 240 7316</div>
</nav>

<!-- hero -->
<section class="abs hero" role="img" aria-label="Electric car plugged into a charging station at sunset">
  <svg class="abs hero-arrow" style="left:55px" viewBox="0 0 20 40"><path d="M16 4 4 20l12 16" fill="none" stroke="#fff" stroke-width="2"/></svg>
  <svg class="abs hero-arrow" style="left:1124px" viewBox="0 0 20 40"><path d="M4 4l12 16L4 36" fill="none" stroke="#fff" stroke-width="2"/></svg>
  <h1 class="abs hero-title">Electric<br>Car Servicing</h1>
  <p class="abs hero-copy">Sed ut perspiciatis unde omnis iste natus error sit amet accusantium doloremque laudantium</p>
  <span class="abs btn hero-btn">BOOK NOW</span>
</section>

<!-- about -->
<section>
  <div class="abs about-bar"></div>
  <div class="abs eyebrow about-eyebrow">About Us</div>
  <h2 class="abs about-title">Our Mission Is To Put<br>Electric Vehicle Charge</h2>
  <p class="abs about-copy">Sed ut perspiciatis unde omnis iste natus error sit voluptatem accusantium doloremque laudantium, totam rem aperiam, eaque ipsa quae ab illo inventore veritatis et quasi architecto beatae vitae dicta sunt explicabo</p>
  <ul class="abs about-list">
    <li>Project Quality Management</li>
    <li>The Ability to Delegate Tasks</li>
    <li>An Ability to Prioritize</li>
  </ul>
  <span class="abs btn about-btn">READ MORE</span>
  <div class="abs about-photo" role="img" aria-label="Man checking his phone beside a charging electric bike"></div>
  <div class="abs exp-tab"><span>20 YEARS OF EXPERIENCE</span></div>
</section>

<!-- services -->
<section>
  <div class="abs eyebrow center" style="top:1116px">Our Services</div>
  <h2 class="abs section-title center" style="top:1138px">We Are Best Service Provider</h2>
  <div class="abs slide-btn" style="left:54px">&#8249;</div>
  <div class="abs slide-btn" style="left:1122px">&#8250;</div>

  <article class="abs svc-card" style="left:129px">
    <div class="svc-body">
      <svg width="40" height="40" viewBox="0 0 40 40"><rect x="6" y="4" width="16" height="24" rx="2" fill="none" stroke="#3fbf12" stroke-width="2.4"/><path d="M14 10l-3 6h5l-3 6" fill="none" stroke="#1649e6" stroke-width="2"/><path d="M22 14h6v12a4 4 0 0 0 8 0V10" fill="none" stroke="#3fbf12" stroke-width="2.4"/><path d="M10 28v6h8v-6" fill="none" stroke="#3fbf12" stroke-width="2.4"/></svg>
      <h3>Tire Rotation</h3>
      <p>Sed ut perspiciatis unde omnis iste natus error sit voluptatem accusantium doloremque laudantium, totam rem aperiam, eaque ipsa sunt explicabo</p>
    </div>
    <div class="svc-foot">VIEW MORE</div>
  </article>
  <article class="abs svc-card" style="left:450px">
    <div class="svc-photo" role="img" aria-label="Driver in a winter coat plugging in a white electric car"></div>
    <div class="svc-foot">VIEW MORE</div>
  </article>
  <article class="abs svc-card" style="left:770px">
    <div class="svc-body">
      <svg width="40" height="40" viewBox="0 0 40 40"><rect x="6" y="8" width="22" height="26" rx="2" fill="none" stroke="#3fbf12" stroke-width="2.4"/><path d="M18 13l-5 8h6l-4 8" fill="none" stroke="#1649e6" stroke-width="2"/><path d="M28 14h4v14h4" fill="none" stroke="#3fbf12" stroke-width="2.4"/><circle cx="31" cy="8" r="3" fill="none" stroke="#3fbf12" stroke-width="2"/></svg>
      <h3>Tire Rotation</h3>
      <p>Sed ut perspiciatis unde omnis iste natus error sit voluptatem accusantium doloremque laudantium, totam rem aperiam, eaque ipsa sunt explicabo</p>
    </div>
    <div class="svc-foot">VIEW MORE</div>
  </article>
</section>

<!-- perks band -->
<section class="abs perks" role="img" aria-label="Dark background of an electric car at a charger">
  <div class="abs perk-num" style="left:159px;top:86px">01</div>
  <div class="abs perk-num" style="left:484px;top:86px">02</div>
  <div class="abs perk-num" style="left:808px;top:86px">03</div>
  <svg class="abs" style="left:129px;top:122px" width="84" height="84" viewBox="0 0 84 84"><path d="M42 2 78 22v40L42 82 6 62V22z" fill="none" stroke="#fff" stroke-width="2"/><rect x="32" y="26" width="16" height="30" rx="2" fill="none" stroke="#3fbf12" stroke-width="2"/><path d="M42 32l-4 7h5l-3 7" fill="none" stroke="#fff" stroke-width="1.6"/></svg>
  <svg class="abs" style="left:453px;top:122px" width="84" height="84" viewBox="0 0 84 84"><path d="M42 2 78 22v40L42 82 6 62V22z" fill="none" stroke="#fff" stroke-width="2"/><circle cx="42" cy="42" r="15" fill="none" stroke="#3fbf12" stroke-width="2"/><path d="M34 44h16M36 38h12" stroke="#fff" stroke-width="1.6"/></svg>
  <svg class="abs" style="left:778px;top:122px" width="84" height="84" viewBox="0 0 84 84"><path d="M42 2 78 22v40L42 82 6 62V22z" fill="none" stroke="#fff" stroke-width="2"/><rect x="30" y="24" width="24" height="28" rx="2" fill="none" stroke="#3fbf12" stroke-width="2"/><circle cx="42" cy="38" r="6" fill="none" stroke="#fff" stroke-width="1.6"/><path d="M42 52v10" stroke="#3fbf12" stroke-width="2"/></svg>
  <h4 class="abs perk-title" style="left:231px;top:80px">Unbeatable Prices</h4>
  <h4 class="abs perk-title" style="left:555px;top:80px">Operational Efficiency</h4>
  <h4 class="abs perk-title" style="left:880px;top:80px">No Upfront Payment</h4>
  <p class="abs perk-copy" style="left:231px;top:116px">Sed ut perspiciatis unde omnis iste natus error sit voluptatem accusantium doloremque laudantium, totam rem aperiam, eaque ipsa quae ab illo inventore...</p>
  <p class="abs perk-copy" style="left:556px;top:116px">Sed ut perspiciatis unde omnis iste natus error sit voluptatem accusantium doloremque laudantium, totam rem aperiam, eaque ipsa quae ab illo inventore...</p>
  <p class="abs perk-copy" style="left:881px;top:116px">Sed ut perspiciatis unde omnis iste natus error sit voluptatem accusantium doloremque laudantium, totam rem aperiam, eaque ipsa quae ab illo inventore...</p>
</section>

<!-- features -->
<section>
  <div class="abs eyebrow center" style="top:1906px">New Technology</div>
  <h2 class="abs section-title center" style="top:1928px">Electric Car Feature</h2>

  <div class="abs feat left" style="left:50px;top:2018px"><h4>Charging Station</h4><p>Sed ut perspiciatis unde omnis iste natus<br>error sit voluptatem accusantium</p></div>
  <div class="abs feat left" style="left:50px;top:2132px"><h4>Fast Charging</h4><p>Sed ut perspiciatis unde omnis iste natus<br>error sit voluptatem accusantium</p></div>
  <div class="abs feat left" style="left:50px;top:2246px"><h4>Charge At Home</h4><p>Sed ut perspiciatis unde omnis iste natus<br>error sit voluptatem accusantium</p></div>

  <div class="abs feat-icon" style="left:369px;top:2018px"><svg width="34" height="34" viewBox="0 0 34 34" fill="none" stroke="#fff" stroke-width="1.6"><rect x="4" y="6" width="14" height="22" rx="2"/><path d="M18 12h5v10a3 3 0 0 0 6 0V8"/><path d="M11 11l-3 6h5l-3 5"/></svg></div>
  <div class="abs feat-icon" style="left:369px;top:2132px"><svg width="34" height="34" viewBox="0 0 34 34" fill="none" stroke="#fff" stroke-width="1.6"><rect x="8" y="4" width="16" height="26" rx="2"/><path d="M17 9l-4 8h6l-4 8"/></svg></div>
  <div class="abs feat-icon" style="left:369px;top:2246px"><svg width="34" height="34" viewBox="0 0 34 34" fill="none" stroke="#fff" stroke-width="1.6"><path d="M3 15 17 4l14 11v15H3z"/><rect x="11" y="17" width="12" height="9" rx="2"/></svg></div>

  <svg class="car" viewBox="0 0 210 310" role="img" aria-label="Top view of a blue electric car with a lightning bolt behind it">
    <path d="M80 0h80L120 120h60L40 310l40-150H10z" fill="#1649e6" opacity=".85"/>
    <rect x="45" y="15" width="120" height="280" rx="48" fill="#2a93bf"/>
  </svg>

  <div class="abs feat-icon" style="left:770px;top:2018px"><svg width="34" height="34" viewBox="0 0 34 34" fill="none" stroke="#fff" stroke-width="1.6"><path d="M4 22l3-8h20l3 8v5H4z"/><circle cx="10" cy="27" r="2"/><circle cx="24" cy="27" r="2"/><path d="M17 4l-3 5h5l-3 4"/></svg></div>
  <div class="abs feat-icon" style="left:770px;top:2132px"><svg width="34" height="34" viewBox="0 0 34 34" fill="none" stroke="#fff" stroke-width="1.6"><circle cx="17" cy="17" r="12"/><path d="M18 9l-5 9h6l-4 8"/></svg></div>
  <div class="abs feat-icon" style="left:770px;top:2246px"><svg width="34" height="34" viewBox="0 0 34 34" fill="none" stroke="#fff" stroke-width="1.6"><circle cx="17" cy="18" r="11"/><path d="M17 11v7l5 3M13 4h8"/></svg></div>

  <div class="abs feat" style="left:849px;top:2018px"><h4>Rapid Charging</h4><p>Sed ut perspiciatis unde omnis iste natus<br>error sit voluptatem accusantium</p></div>
  <div class="abs feat" style="left:849px;top:2132px"><h4>Charge Point Stations</h4><p>Sed ut perspiciatis unde omnis iste natus<br>error sit voluptatem accusantium</p></div>
  <div class="abs feat" style="left:849px;top:2246px"><h4>Charging Timer</h4><p>Sed ut perspiciatis unde omnis iste natus<br>error sit voluptatem accusantium</p></div>
</section>

<!-- testimonial -->
<section>
  <div class="abs testi-photo" role="img" aria-label="Man plugging a charging cable into his car"></div>
  <div class="abs testi-card">
    <svg width="42" height="34" viewBox="0 0 42 34" fill="none" stroke="#3fbf12" stroke-width="2"><path d="M3 33V18C3 8 8 3 16 2M5 18h12v15H3M23 33V18c0-10 5-15 13-16M25 18h12v15H23"/></svg>
    <div class="abs dots"><i></i><i></i><i></i></div>
    <p class="testi-text">Sed ut perspiciatis unde omnis iste natus error sit voluptatem accusantium doloremque laudantium, totam rem aperiam, eaque ipsa quae ab illo inventore veritatis et quasi architecto beatae vitae dicta sunt explicabo. Nemo enim ipsam voluptatem quia voluptas sit aspernatur aut odit aut fugit, sed quia consequuntur magni dolores eos qui ratione voluptatem sequi nesciunt.</p>
    <div style="display:flex;align-items:center;gap:14px;margin-top:14px">
      <div class="avatar" role="img" aria-label="Customer portrait"></div>
      <div style="flex:1"><div style="font-size:12px;font-weight:500;color:#222">NORA ELLISON</div><div style="font-size:9px;color:#888;margin-top:2px">Main Director</div></div>
      <div class="stars">
        <svg width="11" height="11" viewBox="0 0 10 10"><path d="M5 0l1.5 3.2 3.5.4-2.6 2.4.7 3.5L5 7.8 1.9 9.5l.7-3.5L0 3.6l3.5-.4z" fill="#f5b800"/></svg>
        <svg width="11" height="11" viewBox="0 0 10 10"><path d="M5 0l1.5 3.2 3.5.4-2.6 2.4.7 3.5L5 7.8 1.9 9.5l.7-3.5L0 3.6l3.5-.4z" fill="#f5b800"/></svg>
        <svg width="11" height="11" viewBox="0 0 10 10"><path d="M5 0l1.5 3.2 3.5.4-2.6 2.4.7 3.5L5 7.8 1.9 9.5l.7-3.5L0 3.6l3.5-.4z" fill="#f5b800"/></svg>
        <svg width="11" height="11" viewBox="0 0 10 10"><path d="M5 0l1.5 3.2 3.5.4-2.6 2.4.7 3.5L5 7.8 1.9 9.5l.7-3.5L0 3.6l3.5-.4z" fill="#f5b800"/></svg>
        <svg width="11" height="11" viewBox="0 0 10 10"><path d="M5 0l1.5 3.2 3.5.4-2.6 2.4.7 3.5L5 7.8 1.9 9.5l.7-3.5L0 3.6l3.5-.4z" fill="#f5b800"/></svg>
      </div>
    </div>
  </div>
</section>

<!-- video -->
<section class="abs video" role="img" aria-label="Video still of a car charging at a wall station with a city skyline behind">
  <div class="abs play"><svg width="20" height="22" viewBox="0 0 20 22"><path d="M2 1l17 10L2 21z" fill="#fff"/></svg></div>
</section>

<!-- articles -->
<section>
  <div class="abs eyebrow" style="left:129px;top:3273px">Recent Articles</div>
  <h2 class="abs section-title" style="left:129px;top:3293px">Recent Articles and News</h2>
  <article class="abs post" style="left:129px">
    <div class="post-img" style="background:linear-gradient(160deg,#bcd6ee 0%,#e8eef2 40%,#5b8a4a 70%,#e3b33a 100%)" role="img" aria-label="Yellow car at a solar charging station"></div>
    <div class="post-date">February 4, 2022</div>
    <h3 class="post-title">Better than snoozing: driving an EV</h3>
  </article>
  <article class="abs post" style="left:450px">
    <div class="post-img" style="background:linear-gradient(120deg,#3b3d2c 0%,#9ea08a 40%,#e9e9e6 60%,#2b2b2b 100%)" role="img" aria-label="Close-up of a charging plug in a car port"></div>
    <div class="post-date">February 4, 2022</div>
    <h3 class="post-title">Saving the world, one charge at a time</h3>
  </article>
  <article class="abs post" style="left:770px">
    <div class="post-img" style="background:linear-gradient(110deg,#3a3d42 0%,#7d848c 35%,#c5ccd3 60%,#4f87c4 100%)" role="img" aria-label="Blue compact car charging in a parking garage"></div>
    <div class="post-date">February 4, 2022</div>
    <h3 class="post-title">It's time to plug-in to the new road...</h3>
  </article>
</section>

<!-- quote -->
<section>
  <div class="abs quote-photo" role="img" aria-label="Woman with a phone leaning on a car beside a charging station"></div>
  <form class="abs quote-card">
    <h2>Get A Free Quote</h2>
    <p class="sub">Lorem ipsum dolor sit amet, consectetur adipiscing elit, sed do</p>
    <div class="abs field" style="left:29px;top:126px">Your Name</div>
    <div class="abs field" style="left:29px;top:173px">Your Email</div>
    <div class="abs field" style="left:29px;top:221px">Phone Number</div>
    <div class="abs field" style="left:29px;top:268px">Subject Name</div>
    <div class="abs field area" style="left:237px;top:126px">Your Message</div>
    <div class="abs submit" style="left:237px;top:268px">SUBMIT NOW</div>
  </form>
</section>

<!-- footer -->
<footer class="abs footer">
  <div class="abs foot-brand">Volt Ranger Mobile</div>
  <p class="abs foot-about">A premium Html Template for Electric vehicle store and services websites. Get the latest UI/UX landing experience</p>
  <div class="abs socials"><i></i><i></i><i></i><i></i></div>

  <div class="abs foot-col" style="left:450px;top:58px">
    <h5>Quick Links</h5>
    <ul><li>&nbsp;Home</li><li>About</li><li>Vehicles we Support</li><li>iOS / Android apps</li><li>Contact Us</li></ul>
  </div>
  <div class="abs foot-col" style="left:669px;top:58px">
    <h5>Our Services</h5>
    <ul><li>AC Charger Services</li><li>Charge Point Services</li><li>Building Services</li><li>DC Charger Services</li><li>Vehicle Chargers</li></ul>
  </div>
  <div class="abs foot-col" style="left:923px;top:58px">
    <h5>Contacts</h5>
    <div class="foot-contact"><span class="ring"><svg width="8" height="11" viewBox="0 0 10 13"><path d="M5 0a5 5 0 0 0-5 5c0 3.5 5 8 5 8s5-4.5 5-8a5 5 0 0 0-5-5zm0 7a2 2 0 1 1 0-4 2 2 0 0 1 0 4z" fill="#fff"/></svg></span><span>48 Harbor Ln. Clearwater,<br>NY 10820</span></div>
    <div class="foot-contact" style="align-items:center"><span class="ring"><svg width="9" height="11" viewBox="0 0 10 12"><path d="M2 0h2l1 3-1.5 1a6 6 0 0 0 2.5 4l1-1.5 3 1v2a1.5 1.5 0 0 1-1.5 1.5A9 9 0 0 1 .5 1.5 1.5 1.5 0 0 1 2 0z" fill="#fff"/></svg></span><span>+1 (555) 240 7316</span></div>
    <div class="foot-contact" style="align-items:center"><span class="ring"><svg width="11" height="8" viewBox="0 0 12 9"><rect x=".5" y=".5" width="11" height="8" fill="none" stroke="#fff"/><path d="M.5.5 6 5 11.5.5" fill="none" stroke="#fff"/></svg></span><span>info@voltrangermobile</span></div>
  </div>
</footer>
<div class="abs copyright center">Copyright © 2022 <span>Volt Ranger Mobile</span>. All Rights Reserved.</div>

</body>
</html>
```